Business Card Design Project: Classically Trained Singer and Voice Teacher

I am a classically trained singer that performs in Opera and Musical Theater and also teaches private voice lessons in those fields. I am looking for a business card that I can give to casting directors and colleagues, as well as to people who are interested in taking voice lessons from me.

This is sort of like an actors business card so I want my headshot and name to be the main focus.

I was kind of thinking of having the business card be horizontal with my headshot photo on the front taking up roughly half and my information on the same side, and perhaps my name again on the back or some form of my initials. But I am totally open to other options for layout.I would prefer to have a double sided business card, but once again, its not essential.

I am looking for it to look and feel elegant artistic and professional, without looking feminine.

Because of the colors of my headshot I would imagine that it would be predominantly brown and white, but I am totally open to other approaches.feel totally free to crop my headshot so that it fits better into your overall design and layout.

It is highly likely that I will ask the winner of the design to create a flyer for marketing my voice lessons with a similar look.

If you have any questions or clarifications, please feel free to ask.

Target Market(s)

Opera and Musical theater casting directors, colleagues; potential voice lesson students

Industry/Entity Type

Marketing

Requirements
Must have
• These must feature prominently:
- (My Headshot (attached))
- Marlow Keating (my name)

These dont need to be as prominent:
- Baritone
- Private Voice Teacher
- Opera and Musical Theater

Contact Info:
Phone: (555) 347-2816
Email: marlkeat@inboxly.example

Nice to have
• Double sided

```html
<!DOCTYPE html>
<html lang="en">
<head>
<meta charset="utf-8">
<title>Marlow Keating — Business Card</title>
<link rel="stylesheet" href="https://fonts.googleapis.com/css2?family=Alfa+Slab+One&family=Arimo&family=Roboto+Slab:wght@400&display=swap">
<style>
  :root {
    --page: #ffffff;
    --card-blue: #46546d;
    --name-brown: #6b5646;
    --name-outline: #9c9a94;
    --text-white: #ffffff;
    --photo-light: #9a9896;
    --photo-mid: #7e6a55;
    --photo-dark: #4c3f33;
    --shadow: rgba(0, 0, 0, 0.18);
  }
  * { margin: 0; padding: 0; box-sizing: border-box; }
  html, body {
    width: 1008px;
    height: 1200px;
    overflow: hidden;
    background: var(--page);
  }
  .canvas { display: block; width: 1008px; height: 1200px; }
  .card-panel { fill: var(--card-blue); filter: drop-shadow(0 6px 14px var(--shadow)); }
  .name {
    font-family: "Alfa Slab One", "Rockwell", serif;
    fill: var(--name-brown);
    stroke: var(--name-outline);
    paint-order: stroke fill;
    stroke-linejoin: round;
  }
  .name--front { stroke-width: 5px; }
  .name--back { stroke-width: 9px; }
  .phone {
    font-family: "Arimo", Arial, sans-serif;
    font-size: 40px;
    fill: var(--text-white);
  }
  .email {
    font-family: "Roboto Slab", "Rockwell", serif;
    font-size: 27px;
    fill: var(--text-white);
  }
  .role {
    font-family: "Roboto Slab", "Rockwell", serif;
    font-size: 31px;
    fill: var(--text-white);
  }
</style>
</head>
<body>
<svg class="canvas" viewBox="0 0 1008 1200" xmlns="http://www.w3.org/2000/svg">
  <defs>
    <linearGradient id="headshot-tones" x1="0" y1="0" x2="1" y2="1">
      <stop offset="0" stop-color="var(--photo-light)"/>
      <stop offset="0.55" stop-color="var(--photo-mid)"/>
      <stop offset="1" stop-color="var(--photo-dark)"/>
    </linearGradient>
  </defs>

  <!-- Front of card -->
  <g class="card card--front">
    <rect class="card-panel" x="55" y="50" width="883" height="512"/>
    <rect class="headshot" x="487" y="50" width="451" height="512" fill="url(#headshot-tones)"
          role="img" aria-label="Headshot of Marlow Keating in a brown jacket and striped shirt"/>
    <text class="name name--front" x="80" y="334" font-size="54" textLength="382" lengthAdjust="spacingAndGlyphs">MARLOW</text>
    <text class="name name--front" x="80" y="419" font-size="84" textLength="382" lengthAdjust="spacingAndGlyphs">KEATING</text>
    <text class="phone" x="271" y="481" text-anchor="middle">(555) 347-2816</text>
    <text class="email" x="271" y="516" text-anchor="middle" textLength="382" lengthAdjust="spacingAndGlyphs">marlkeat@inboxly.example</text>
  </g>

  <!-- Back of card -->
  <g class="card card--back">
    <rect class="card-panel" x="55" y="628" width="883" height="510"/>
    <text class="name name--back" x="120" y="794" font-size="118" textLength="752" lengthAdjust="spacingAndGlyphs">MARLOW</text>
    <text class="name name--back" x="124" y="962" font-size="190" textLength="748" lengthAdjust="spacingAndGlyphs">KEATING</text>
    <text class="role" x="913" y="1030" text-anchor="end">Baritone</text>
    <text class="role" x="913" y="1064" text-anchor="end">Private Voice Teacher</text>
    <text class="role" x="913" y="1098" text-anchor="end">Opera &amp; Musical Theater</text>
  </g>
</svg>
</body>
</html>
```